Label Design For Vitamin C Serum for Larkwind Skin Care

I need a label design for a bottle similar to this:

https://www.tradelumo-market.example/item/Sample-Face-Serum-Bottle/50000000001.html

Industry/Entity Type

Skin Care Product

Font styles to use
Other font styles liked:
• use logo and use anything standard for label text

Colors
000000

Requirements
Must have
• 20% Vitamin C Brightening Serum
• 30 ML
• On back of label:
• Vitamin C serum is a potent antioxidant designed to help minimize the damaging effects of free oxygen radicals.
• This formulation will help restore skin tone and youthful appearance to the skin.
• Apply 2-3 drops of serum to desired areas. Massage with fingertips.
Nice to have
• I want to use the GOLD LOGO with BLACK LABEL

```html
<!DOCTYPE html>
<html lang="en">
<head>
<meta charset="utf-8">
<title>Larkwind Skin Care – Vitamin C Serum Labels</title>
<link href="https://fonts.googleapis.com/css2?family=Playfair+Display:wght@400;700&family=Montserrat:wght@300;400;500&display=swap" rel="stylesheet">
<style>
  :root {
    --page: #ffffff;
    --label: #0d0d0d;
    --label-edge: #1c1c1c;
    --gold: #c9a15a;
    --text-light: #d9d9d9;
    --text-muted: #a8a8a8;
    --pill: #e0a246;
    --pill-text: #3a2408;
    --badge: #cfcfcf;
    --badge-fill: #d18f2c;
  }
  * { margin: 0; padding: 0; box-sizing: border-box; }
  html, body { width: 1200px; height: 857px; overflow: hidden; background: var(--page); }
  .canvas {
    position: relative; width: 1200px; height: 857px;
    display: flex; justify-content: center; align-items: center; gap: 70px;
  }
  .label {
    position: relative; width: 172px; height: 270px;
    background: var(--label); border: 1px solid var(--label-edge);
  }
  /* front */
  .brand {
    position: absolute; top: 20px; left: 0; right: 0; text-align: center;
    font-family: "Playfair Display", serif; font-weight: 400;
    color: var(--gold); font-size: 18px; letter-spacing: 1px; line-height: 1.2;
  }
  .brand-sub {
    position: absolute; top: 47px; left: 10px; right: 10px;
    display: flex; align-items: center; gap: 5px;
    font-family: "Montserrat", sans-serif; font-weight: 400;
    color: var(--gold); font-size: 10px; letter-spacing: 0.5px; white-space: nowrap;
  }
  .brand-sub::before, .brand-sub::after { content: ""; flex: 1; height: 1px; background: var(--gold); }
  .product-block {
    position: absolute; top: 100px; left: 0; right: 0; text-align: center;
  }
  .strength {
    font-family: "Playfair Display", serif; font-weight: 700;
    color: var(--gold); font-size: 26px; line-height: 1.1;
  }
  .divider {
    width: 60px; height: 1px; margin: 8px auto; background: var(--gold);
  }
  .product-name {
    font-family: "Playfair Display", serif; font-weight: 700;
    color: var(--text-light); font-size: 17px; line-height: 1.2; white-space: nowrap;
  }
  .product-type {
    margin-top: 4px;
    font-family: "Playfair Display", serif; font-weight: 400; font-size: 9px;
    color: var(--text-light); white-space: nowrap;
  }
  .volume {
    position: absolute; bottom: 20px; left: 0; right: 0; text-align: center;
    font-family: "Playfair Display", serif; font-size: 10px; color: var(--text-light);
  }
  /* back */
  .claims {
    position: absolute; top: 22px; left: 14px; right: 12px; list-style: none;
    font-family: "Montserrat", sans-serif; font-weight: 300;
    font-size: 6px; line-height: 1.5; color: var(--text-muted); text-transform: uppercase;
  }
  .claims li { position: relative; padding-left: 7px; margin-bottom: 9px; }
  .claims li::before { content: "•"; position: absolute; left: 0; }
  .tagline {
    position: absolute; top: 162px; left: 20px; right: 20px; height: 12px;
    border-radius: 6px; background: var(--pill);
    font-family: "Montserrat", sans-serif; font-size: 6px; color: var(--pill-text);
    display: flex; align-items: center; justify-content: center; white-space: nowrap;
  }
  .badges {
    position: absolute; bottom: 28px; left: 16px; right: 16px;
    display: flex; justify-content: space-between; align-items: center;
  }
</style>
</head>
<body>
<main class="canvas">
  <section class="label label-front">
    <div class="brand">LARKWIND</div>
    <div class="brand-sub">SKIN CARE</div>
    <div class="product-block">
      <div class="strength">20%</div>
      <div class="divider"></div>
      <div class="product-name">Vitamin C</div>
      <div class="product-type">Brightening Serum</div>
    </div>
    <div class="volume">1 fl oz / 30 ml</div>
  </section>

  <section class="label label-back">
    <ul class="claims">
      <li>Vitamin C serum is a potent antioxidant designed to help minimize the damaging effects of free oxygen radicals.</li>
      <li>This formulation will help restore skin tone and youthful appearance to the skin.</li>
      <li>Apply 2-3 drops of serum to desired areas. Massage with fingertips.</li>
    </ul>
    <div class="tagline">Professional Acid Anti-Aging Serum</div>
    <div class="badges">
      <svg width="22" height="22" role="img" aria-label="Quality badge"><circle cx="11" cy="11" r="10" fill="none" stroke="var(--badge)" stroke-width="1.2"/></svg>
      <svg width="24" height="24" role="img" aria-label="Certification badge"><circle cx="12" cy="12" r="11" fill="var(--badge-fill)"/></svg>
      <svg width="24" height="22" role="img" aria-label="Cruelty-free badge"><circle cx="12" cy="11" r="9" fill="none" stroke="var(--badge)" stroke-width="1.2"/></svg>
      <svg width="18" height="22" role="img" aria-label="Period after opening badge"><rect x="2" y="4" width="14" height="14" rx="2" fill="none" stroke="var(--badge)" stroke-width="1.2"/></svg>
    </div>
  </section>
</main>
</body>
</html>
```